We require a Squarespace web design for Mossfield Cannabis Website.
We are an urban community retail cannabis store. We have turn tables set up playing old hip hop/house music to create a lounge vibe. The store is very urban, dark and sexy. We have a couple of concepts that we like. One is a dark stone background and smoke rising up. Such as the link here. https://dev.lumo.varnell.quixo.com/products/
The other is using the black and white map of our community.
We would like to have any concept include the logo on the turntable with the logo spinning like a record and the words MOSSFIELD CANNABIS also spinning around it (such as in the attached giff.)
We tend to gravitate toward black and white and gold for the colours.
5817 Harwick Boulevard West,
Scarborough, ON M4R 7K2
(416) 738-LEAF
Hours of Operation
Open Daily 10:00 - 10:00

```html
<!DOCTYPE html>
<html lang="en">
<head>
<meta charset="utf-8">
<title>Mossfield Cannabis</title>
<link href="https://fonts.googleapis.com/css2?family=Bebas+Neue&family=Arimo:ital,wght@0,400;1,400&display=swap" rel="stylesheet">
<style>
:root{
  --bg:#111216;
  --gold:#d7bf62;
  --band:#d8bf69;
  --white:#ffffff;
  --text:#e6e6e6;
  --rule:#2a2b30;
}
*{margin:0;padding:0;box-sizing:border-box}
html,body{width:1200px;height:3639px;overflow:hidden;background:var(--bg)}
body{position:relative;font-family:"Arimo",Arial,sans-serif;color:var(--text)}
.abs{position:absolute}
.display{font-family:"Bebas Neue","Oswald",sans-serif;font-weight:400}

/* header */
.brand{display:flex;align-items:center;gap:14px}
.brand-mark{border:2px solid var(--gold);border-radius:50%}
.brand-name{font-family:"Bebas Neue",sans-serif;color:var(--gold);line-height:1}
.brand-name .main{display:block;letter-spacing:8px}
.brand-name .sub{display:block;letter-spacing:6px;text-align:right}
.site-brand{left:112px;top:34px}
.site-brand .brand-mark{width:86px;height:86px}
.site-brand .main{font-size:34px}
.site-brand .sub{font-size:15px}
.nav{top:62px;left:560px;width:530px;display:flex;justify-content:space-between}
.nav a{font-family:"Bebas Neue",sans-serif;font-size:20px;color:var(--white);text-decoration:none;letter-spacing:.5px}
.nav a.active{color:var(--gold)}

/* hero */
.hero{left:112px;top:153px;width:978px;height:546px;
  background:radial-gradient(ellipse at 50% 40%,#3d6b2d 0%,#1f3a18 35%,#0a120a 70%,#030503 100%)}
.hero-title{left:112px;top:455px;width:978px;text-align:center;font-size:56px;color:var(--white);letter-spacing:1px}
.hero-sub{left:112px;top:532px;width:978px;text-align:center;font-size:18px;line-height:30px;color:var(--white)}

/* feature rows */
.photo{width:488px;height:553px}
.photo-smoke{left:112px;top:791px;background:linear-gradient(135deg,#2e4a22 0%,#8c6a55 35%,#c9a48e 60%,#3a2e2a 100%)}
.photo-bud{left:600px;top:1416px;background:radial-gradient(ellipse at 55% 45%,#8e977b 0%,#6a6453 45%,#514452 80%,#3d3440 100%)}
.photo-oil{left:112px;top:2046px;background:linear-gradient(180deg,#eadfc8 0%,#b9b27c 35%,#4f8a2f 60%,#8a6b45 100%)}
.eyebrow{font-size:25px;color:var(--gold);letter-spacing:.5px}
.headline{font-size:40px;color:var(--gold);letter-spacing:.5px}
.copy{width:390px;font-size:13px;line-height:25px;color:var(--text);text-align:justify}
.btn{display:flex;align-items:center;justify-content:center;font-family:"Bebas Neue",sans-serif;font-size:21px;color:var(--white);background:var(--gold);width:155px;height:53px;letter-spacing:.5px}

/* testimonials */
.quote{width:455px;font-style:italic;font-size:21px;line-height:32px;color:var(--text)}
.quote .mark{font-family:"Bebas Neue",sans-serif;font-style:normal;font-size:34px;color:var(--white);line-height:0;vertical-align:-6px}
.quote-name{font-size:21px;color:var(--white)}

/* band */
.band{left:0;top:2924px;width:1200px;height:341px;background:var(--band)}
.band-badge{left:113px;top:2927px;width:350px;height:322px;background:radial-gradient(circle at 50% 50%,#e4cf85 0%,#d3b85e 70%,#d8bf69 100%);border-radius:50%}
.band-text{left:511px;top:3023px;font-size:27px;line-height:38px;color:var(--white)}
.btn-outline{left:514px;top:3122px;width:149px;height:51px;border:3px solid var(--white);background:transparent}

/* footer */
.foot-brand{left:113px;top:3321px}
.foot-brand .brand-mark{width:112px;height:112px}
.foot-brand .main{font-size:42px}
.foot-brand .sub{font-size:18px}
.social{left:250px;top:3449px;display:flex;gap:9px}
.social span{width:35px;height:35px;border:2px solid var(--white);border-radius:50%}
.foot-links{left:614px;top:3328px;list-style:none}
.foot-links li{font-size:15px;line-height:33.7px;color:var(--white)}
.foot-info{left:829px;top:3328px;font-size:15px;color:var(--white)}
.foot-info p{line-height:21px;margin-bottom:12px}
.rule{left:112px;top:3552px;width:978px;height:1px;background:var(--rule)}
.copyright{left:0;top:3586px;width:1200px;text-align:center;font-size:15px;color:var(--white)}
</style>
</head>
<body>

<header>
  <div class="abs brand site-brand">
    <span class="brand-mark"></span>
    <span class="brand-name"><span class="main">MOSSFIELD</span><span class="sub">CANNABIS</span></span>
  </div>
  <nav class="abs nav">
    <a class="active" href="#">Home</a>
    <a href="#">About Us</a>
    <a href="#">Services</a>
    <a href="#">News</a>
    <a href="#">Contact Us</a>
  </nav>
</header>

<section>
  <div class="abs hero" role="img" aria-label="Cannabis leaves against a dark background"></div>
  <h1 class="abs hero-title display">MOSSFIELD CANNABIS</h1>
  <p class="abs hero-sub display">SED UT PERSPICIATIS UNDE OMNIS ISTE NATUS ERROR SIT VOLUPTATEM ACCUSANTIUM<br>DOLOREMQUE LAUDANTIUM, TOTAM REM APERIAM</p>
</section>

<section>
  <div class="abs photo photo-smoke" role="img" aria-label="Woman exhaling smoke"></div>
  <p class="abs eyebrow display" style="left:671px;top:884px">ABOUT US</p>
  <h2 class="abs headline display" style="left:671px;top:923px">MOSSFIELD CANNABIS</h2>
  <p class="abs copy" style="left:671px;top:988px">Sed ut perspiciatis unde omnis iste natus error sit voluptatem accusantium doloremque laudantium, totam rem aperiam, eaque ipsa quae ab illo inventore veritatis et quasi architecto beatae vitae dicta sunt explicabo. Nemo enim ipsam voluptatem quia voluptas sit aspernatur aut odit aut fugit, sed quia consequuntur dolores eos qui ratione voluptatem sequi nesciunt.</p>
  <a class="abs btn" style="left:675px;top:1172px">READ MORE</a>
</section>

<section>
  <p class="abs eyebrow display" style="left:140px;top:1527px">MOSSFIELD CANNABIS</p>
  <h2 class="abs headline display" style="left:140px;top:1566px">SED UT PERSPICIATIS UNDE</h2>
  <p class="abs copy" style="left:140px;top:1631px">Sed ut perspiciatis unde omnis iste natus error sit voluptatem accusantium doloremque laudantium, totam rem aperiam, eaque ipsa quae ab illo inventore veritatis et quasi architecto beatae vitae dicta sunt explicabo. Nemo enim ipsam voluptatem quia voluptas sit aspernatur aut odit aut fugit, sed quia consequuntur dolores eos qui ratione voluptatem sequi nesciunt.</p>
  <a class="abs btn" style="left:144px;top:1814px">READ MORE</a>
  <div class="abs photo photo-bud" role="img" aria-label="Close-up of a frosted cannabis bud"></div>
</section>

<section>
  <div class="abs photo photo-oil" role="img" aria-label="Jar of cannabis oil beside green leaves"></div>
  <p class="abs eyebrow display" style="left:671px;top:2139px">MOSSFIELD CANNABIS</p>
  <h2 class="abs headline display" style="left:671px;top:2177px">SED UT PERSPICIATIS UNDE</h2>
  <p class="abs copy" style="left:671px;top:2243px">Sed ut perspiciatis unde omnis iste natus error sit voluptatem accusantium doloremque laudantium, totam rem aperiam, eaque ipsa quae ab illo inventore veritatis et quasi architecto beatae vitae dicta sunt explicabo. Nemo enim ipsam voluptatem quia voluptas sit aspernatur aut odit aut fugit, sed quia consequuntur dolores eos qui ratione voluptatem sequi nesciunt.</p>
  <a class="abs btn" style="left:675px;top:2427px">READ MORE</a>
</section>

<section>
  <blockquote class="abs quote" style="left:112px;top:2716px"><span class="mark">"</span> Sed ut perspiciatis unde omnis iste natus error sit voluptatem accu santium doloremque laudanti um, totam rem aperiam, <span class="mark">"</span></blockquote>
  <p class="abs quote-name display" style="left:112px;top:2834px">DANA REEVES</p>
  <blockquote class="abs quote" style="left:638px;top:2716px"><span class="mark">"</span> Sed ut perspiciatis unde omnis iste natus error sit voluptatem accu santium doloremque laudanti um, totam rem aperiam, <span class="mark">"</span></blockquote>
  <p class="abs quote-name display" style="left:638px;top:2834px">DANA REEVES</p>
</section>

<section>
  <div class="abs band"></div>
  <div class="abs band-badge" role="img" aria-label="Circular hand-lettered welcome badge"></div>
  <p class="abs band-text display">SED UT PERSPICIATIS UNDE OMNIS ISTE NATUS<br>SIT VOLUPTATEM ACCUSANTIUM DOLOREMQUE LAUDANTIUM</p>
  <a class="abs btn btn-outline">READ MORE</a>
</section>

<footer>
  <div class="abs brand foot-brand">
    <span class="brand-mark"></span>
    <span class="brand-name"><span class="main">MOSSFIELD</span><span class="sub">CANNABIS</span></span>
  </div>
  <div class="abs social" aria-label="Social links"><span></span><span></span><span></span><span></span></div>
  <ul class="abs foot-links">
    <li>Home</li><li>About Us</li><li>Services</li><li>News</li><li>Contact Us</li>
  </ul>
  <div class="abs foot-info">
    <p>5817 Harwick Boulevard West,<br>Scarborough, ON M4R 7K2</p>
    <p>(416) 738-LEAF</p>
    <p>Hours of Operation</p>
    <p>Open Daily 10:00 - 10:00</p>
  </div>
  <div class="abs rule"></div>
  <p class="abs copyright">© Copyright 2021.All Rights Reserved</p>
</footer>

</body>
</html>
```